Calm and Compass Health Flyer (new business startup)

One page...clear enough to be read if faxed. This mental health clinic treats depression/anxiety in kids and adults. It also treats opiate and alcohol addiction. It's in downtown Elmira, NY and the owner of the clinic is from Elmira NY, where it's located. This clinic does not take health insurance, so it charges a low rate of $75 a visit once they pay the $125 starting fee.

Target Market(s)

doctors offices, new patients

Industry/Entity Type

Doctor

Requirements
Must have
• see microsoft word document. pdf is printed on the company letterhead.
Nice to have
• a simplified map would be nice. if you can include the building it would be a plus. The same two fonts were used in the business cards and letter head (kennedy small caps boo*) and Refrigerator Delux.

```html
<!DOCTYPE html>
<html lang="en">
<head>
<meta charset="utf-8">
<title>Calm and Compass Health Flyer</title>
<link href="https://fonts.googleapis.com/css2?family=Barlow:ital,wght@0,300;0,400;0,500;0,600;0,700;1,300;1,400;1,500;1,700&family=Crimson+Pro:wght@600;700&display=swap" rel="stylesheet">
<style>
  :root {
    --bg: #e4e5ea;
    --orange: #f05a24;
    --navy: #0f1f7a;
    --navy-deep: #05082a;
    --sky: #29a8e0;
    --sky-text: #1ea1dc;
    --ink: #111111;
    --grey-row: #e3e3e3;
    --white: #ffffff;
  }
  * { box-sizing: border-box; margin: 0; padding: 0; }
  html, body { width: 1200px; height: 1200px; overflow: hidden; }
  body { background: var(--bg); font-family: "Barlow", Arial, sans-serif; position: relative; }

  .flyer { position: absolute; left: 256px; top: 117px; width: 686px; height: 888px; background: var(--white); overflow: hidden; }
  .flyer > * { position: absolute; }

  .top-rule { left: 0; top: 0; width: 686px; height: 13px; background: var(--orange); }

  .hero { left: 0; top: 13px; width: 686px; height: 322px;
    background: linear-gradient(90deg, var(--navy-deep) 35%, #0c1668 60%, var(--navy) 100%); }
  .hero-photo { left: 0; top: 13px; width: 281px; height: 322px;
    background: linear-gradient(100deg, #0a0a0a 0%, #5a5e6a 40%, #b9bcc6 55%, #3a3d46 80%, #111 100%); }

  .brand { left: 292px; top: 13px; width: 380px; height: 95px; background: var(--white);
    display: flex; align-items: center; justify-content: center; gap: 10px; }
  .brand-dot { width: 30px; height: 30px; border-radius: 50%; background: var(--orange); flex: none; }
  .brand-name { font-weight: 700; font-size: 22px; color: var(--orange); letter-spacing: -0.2px; }

  .hours { left: 292px; top: 114px; width: 380px; text-align: center; color: var(--white); font-size: 18px; font-weight: 500; }

  .tagline { left: 306px; top: 226px; color: var(--white); font-style: italic; line-height: 39px; }
  .tagline .lead { display: block; color: var(--orange); font-weight: 700; font-size: 39px; }
  .tagline .rest { display: block; font-weight: 300; font-size: 38px; letter-spacing: 1px; }

  .intro-panel { left: 0; top: 335px; width: 281px; height: 293px; background: var(--orange); }
  .intro-text { left: 17px; top: 355px; width: 248px; color: var(--white); font-style: italic; font-weight: 500; font-size: 16.5px; line-height: 21.5px; }

  .map { left: 0; top: 628px; width: 281px; height: 177px;
    background: linear-gradient(160deg, #eceef0 0%, #e4e7ea 60%, #cfe3f2 75%, #e9ebee 100%); }
  .building { left: 50px; top: 520px; width: 162px; height: 162px; border-radius: 50%; border: 4px solid var(--white);
    background: linear-gradient(180deg, #9fc4e6 0%, #9fc4e6 22%, #7a4a3c 23%, #5c3a30 75%, #8d8f94 100%); }

  .details { left: 296px; top: 355px; width: 380px; color: var(--ink); font-size: 18px; font-weight: 500; }
  .label { color: var(--sky-text); font-weight: 600; }
  .cond-title { margin-top: 9px; font-size: 18px; }
  .conditions { display: grid; grid-template-columns: 142px 1fr; margin-top: 1px; line-height: 21.5px; }
  .conditions ul { list-style: none; }
  .conditions ul.right { margin-top: 20px; }
  .conditions li { display: flex; align-items: center; gap: 5px; }
  .tick { width: 14px; height: 14px; flex: none; }

  .price-head { left: 292px; width: 380px; height: 34px; color: var(--white); font-weight: 600; font-size: 26px; line-height: 34px; padding-left: 30px; }
  .price-head.eval { top: 507px; background: var(--sky); }
  .price-head.visit { top: 593px; background: var(--orange); }
  .price-row { left: 292px; width: 380px; height: 38px; background: var(--grey-row);
    display: flex; align-items: center; padding: 0 36px 0 30px; font-weight: 600; font-size: 17px; color: var(--ink); }
  .price-row.eval { top: 543px; }
  .price-row.visit { top: 629px; }
  .leader { flex: 1; border-bottom: 2px dotted var(--ink); margin: 0 4px; transform: translateY(4px); }

  .promise { left: 299px; top: 687px; font-size: 17.5px; font-weight: 500; color: var(--ink); }
  .note { left: 295px; top: 714px; width: 380px; font-size: 12.5px; font-style: italic; font-weight: 400; line-height: 16px; color: var(--ink); }

  .provider { left: 281px; top: 778px; width: 405px; height: 55px; background: var(--navy); color: var(--white);
    font-family: "Crimson Pro", "Times New Roman", serif; text-align: center; padding-top: 7px; z-index: 2; }
  .provider-name { font-size: 21px; font-weight: 700; letter-spacing: 0.8px; line-height: 22px; }
  .provider-role { font-size: 13px; font-weight: 600; line-height: 16px; }

  .contact-band { left: 0; top: 805px; width: 686px; height: 83px; background: var(--sky); }
  .contact { color: var(--white); font-size: 13px; font-weight: 600; line-height: 15px; display: flex; gap: 6px; }
  .contact svg { width: 12px; height: 12px; flex: none; margin-top: 1px; }
  .contact-lines div { display: flex; align-items: center; gap: 6px; }
  .contact.address { left: 40px; top: 831px; }
  .contact.phones { left: 313px; top: 847px; }
  .contact.web { left: 490px; top: 847px; }
</style>
</head>
<body>
<main class="flyer">
  <div class="top-rule"></div>
  <div class="hero"></div>
  <div class="hero-photo" role="img" aria-label="Black and white photo of a young girl with long hair seen from behind, head bowed"></div>

  <div class="brand"><span class="brand-dot"></span><span class="brand-name">CALM AND COMPASS HEALTH</span></div>
  <p class="hours">HOURS: Mondays and Saturdays 9am-4pm</p>

  <h1 class="tagline"><span class="lead">Improving lives,</span><span class="rest">one person at a time.</span></h1>

  <div class="intro-panel"></div>
  <p class="intro-text">Calm and Compass Health Clinic treats depression and anxiety in individuals from ages 6 years old and up. We also treat substance use disorders, including, but not limited to, opiate and alcohol addictions.</p>

  <div class="map" role="img" aria-label="Simplified street map of the downtown area with a pin marking the clinic location near the river"></div>
  <div class="building" role="img" aria-label="Photo of the brick clinic building on a downtown street corner"></div>

  <section class="details">
    <p class="ages"><span class="label">AGES:</span>&nbsp; 6 years old and up</p>
    <p class="cond-title label">CONDITIONS TREATED:</p>
    <div class="conditions">
      <ul>
        <li><svg class="tick" viewBox="0 0 14 14"><path d="M1 7.5l4 4L13 2" fill="none" stroke="var(--orange)" stroke-width="2"/></svg>Depression</li>
        <li><svg class="tick" viewBox="0 0 14 14"><path d="M1 7.5l4 4L13 2" fill="none" stroke="var(--sky)" stroke-width="2"/></svg>Anxiety</li>
        <li><svg class="tick" viewBox="0 0 14 14"><path d="M1 7.5l4 4L13 2" fill="none" stroke="var(--orange)" stroke-width="2"/></svg>PTSD</li>
        <li><svg class="tick" viewBox="0 0 14 14"><path d="M1 7.5l4 4L13 2" fill="none" stroke="var(--sky)" stroke-width="2"/></svg>ADHD</li>
      </ul>
      <ul class="right">
        <li><svg class="tick" viewBox="0 0 14 14"><path d="M1 7.5l4 4L13 2" fill="none" stroke="var(--orange)" stroke-width="2"/></svg>Addiction</li>
        <li><svg class="tick" viewBox="0 0 14 14"><path d="M1 7.5l4 4L13 2" fill="none" stroke="var(--sky)" stroke-width="2"/></svg>Bipolar</li>
        <li><svg class="tick" viewBox="0 0 14 14"><path d="M1 7.5l4 4L13 2" fill="none" stroke="var(--orange)" stroke-width="2"/></svg>Childhood Mood Disorders</li>
      </ul>
    </div>
  </section>

  <h2 class="price-head eval">PSYCHIATRIC EVALUATION</h2>
  <p class="price-row eval"><span>(45 mins)</span><span class="leader"></span><span>* $125</span></p>
  <h2 class="price-head visit">PSYCHIATRIC OFFICE VISIT</h2>
  <p class="price-row visit"><span>(15 mins)</span><span class="leader"></span><span>* $75</span></p>

  <p class="promise">We work for you, not the insurance companies</p>
  <p class="note">*Although we do not partner with any Health Insurance Companies at this time, a bill will be provided to you at the time of service for you to submit to your insurance company.</p>

  <div class="contact-band"></div>
  <div class="provider">
    <p class="provider-name">DANIEL REYES, RPA, PLLC</p>
    <p class="provider-role">Psychiatric Physician Assistant (PA-C, PSY-CAQ)</p>
  </div>

  <div class="contact address">
    <svg viewBox="0 0 12 12"><path d="M6 0.5a4 4 0 0 0-4 4c0 3 4 7 4 7s4-4 4-7a4 4 0 0 0-4-4z" fill="var(--white)"/><circle cx="6" cy="4.5" r="1.4" fill="var(--sky)"/></svg>
    <div class="contact-lines"><div>240 W. Water St #118</div><div>Brookmere, NY 14000</div><div>with Dr. Helen Marsh</div></div>
  </div>

  <div class="contact phones">
    <div class="contact-lines">
      <div><svg viewBox="0 0 12 12"><path d="M2.5 1l2 2.5-1 1.3a7 7 0 0 0 3.7 3.7l1.3-1 2.5 2-1 1.5C5.5 11 1 6.5 1 2z" fill="var(--white)"/></svg>607-555-0142</div>
      <div><svg viewBox="0 0 12 12"><rect x="3" y="1" width="6" height="3" fill="var(--white)"/><rect x="1" y="4.5" width="10" height="5" rx="1" fill="var(--white)"/><rect x="3" y="8" width="6" height="3" fill="var(--white)" stroke="var(--sky)" stroke-width="0.8"/></svg>607-555-0178</div>
    </div>
  </div>

  <div class="contact web">
    <div class="contact-lines">
      <div><svg viewBox="0 0 12 12"><rect x="1" y="2.5" width="10" height="7" fill="none" stroke="var(--white)" stroke-width="1.2"/><path d="M1 3l5 4 5-4" fill="none" stroke="var(--white)" stroke-width="1.2"/></svg>dreyes@calmcompass.com</div>
      <div><svg viewBox="0 0 12 12"><circle cx="6" cy="6" r="5" fill="none" stroke="var(--white)" stroke-width="1.2"/><ellipse cx="6" cy="6" rx="2.2" ry="5" fill="none" stroke="var(--white)" stroke-width="1"/><path d="M1 6h10" stroke="var(--white)" stroke-width="1"/></svg>www.calm-compass.com</div>
    </div>
  </div>
</main>
</body>
</html>
```